Ridgecrest Rapid Wash Web Design

We are looking for a web design that highlights our state of the art fully automated commercial vehicle washing equipment. Similar system to a car wash however this system is meant for the largest vehicles on our roadways. Transport trucks with or without a trailer, busses both highway and school, RV's from 5th wheel type to A Class. Cement trucks, dump trucks, vac trucks, fuel trucks etc. Pick ups with utility trailers...Refrigerator truck clean outs.
Ridgecrest Rapid Wash will wash your vehicle quickly and with a minimal impact on the environment

Home page
About us
Why Ridgecrest
Services and pricing
Videos of wash system
Fleets
contact us

Target Market(s)

Commercial vehicle owners and operators as well as corporate fleets. Includes busses, municipal, school and highway.both school and

Industry/Entity Type

transportation

Coding

Coded - Design and coding required

Number of Pages Required

5+ page

Font styles to use
Sans Serif

Colors
0054AA
0677BA
7BADD7
CADEEF
E8F1F8

Requirements
Must have
• Welcome page,why us page which describes the financial and environmental benefits. payment processing page, contact us page, Services which is washing vehicles and greasing for commercial vehicles that want that service and grease
Nice to have
• pictures of both clean and dirty commercial vehicles ie. before and after

```html
<!DOCTYPE html>
<html lang="en">
<head>
<meta charset="utf-8">
<title>Ridgecrest Rapid Wash</title>
<link href="https://fonts.googleapis.com/css2?family=Poppins:ital,wght@0,400;0,500;0,600;0,700;1,600;1,700;1,800;1,900&display=swap" rel="stylesheet">
<style>
:root{
  --navy:#0a1478;
  --navy-deep:#07105c;
  --royal:#1c2fa3;
  --gray-band:#6b6b6b;
  --ring:#6e6e6e;
  --ink:#333;
  --line:#cfcfcf;
  --soft:#f1f1f1;
  --white:#fff;
  --star:#f07a1a;
}
*{margin:0;padding:0;box-sizing:border-box}
html,body{width:1200px;height:4721px;overflow:hidden}
body{font-family:"Poppins",sans-serif;color:var(--ink);background:var(--white);position:relative}
section,header,footer{position:absolute;left:0;width:1200px}
.abs{position:absolute}
.heading{font-family:"Poppins",sans-serif;font-style:italic;font-weight:900;color:var(--navy);text-transform:uppercase;letter-spacing:.5px}

/* header */
.site-header{top:0;height:105px;background:var(--gray-band)}
.brand{left:74px;top:30px;color:var(--white);font-weight:700;font-size:22px;line-height:1.1}
.brand small{display:block;font-size:12px;letter-spacing:2px;font-weight:700}
.nav{right:74px;top:45px;display:flex;gap:26px;font-size:12px;font-weight:700;font-style:italic;color:var(--white);text-transform:uppercase}
.nav .active{text-decoration:underline;text-underline-offset:4px}

/* hero */
.hero{top:105px;height:549px}
.hero-media{position:absolute;inset:0;background:radial-gradient(ellipse at 50% 45%,#4d5bd0 0%,#2a37a8 35%,#141e78 75%,#0b1258 100%)}
.hero-title{top:125px;width:100%;text-align:center;color:var(--white);font-style:italic;font-weight:900;text-transform:uppercase;line-height:1}
.hero-title .l1{font-size:70px;display:block;letter-spacing:2px}
.hero-title .l2{font-size:50px;display:block;margin-top:6px;letter-spacing:2px}
.hero-text{top:258px;left:280px;width:640px;text-align:center;color:var(--white);font-size:21px;font-weight:600;line-height:30px}
.hero-btns{top:363px;width:100%;display:flex;justify-content:center;gap:14px}
.btn-ghost{border:2px solid var(--white);color:var(--white);font-size:13px;font-weight:700;width:152px;height:48px;display:flex;align-items:center;justify-content:center;text-transform:uppercase}
.dots{top:503px;width:100%;display:flex;justify-content:center;gap:10px}
.dots span{width:10px;height:10px;background:var(--white)}
.dots span.on{background:#36b0ff;border-radius:50%}

/* services */
.services{top:654px;height:522px}
.services .heading{top:55px;width:100%;text-align:center;font-size:40px}
.svc{top:146px;width:360px;text-align:center}
.svc-ring{width:174px;height:174px;border-radius:50%;background:var(--ring);margin:0 auto;display:flex;align-items:center;justify-content:center}
.svc-ring div{width:154px;height:154px;border-radius:50%;background:var(--navy);display:flex;align-items:center;justify-content:center}
.svc h3{font-style:italic;font-weight:800;font-size:20px;color:var(--navy);text-transform:uppercase;margin-top:22px}
.svc p{font-size:13px;line-height:22px;margin:14px auto 0;width:330px}

/* mission */
.mission{top:1176px;height:396px}
.mission-media{position:absolute;inset:0;background:linear-gradient(90deg,#1b2a9c 0%,#3344b8 30%,#3a4cc0 50%,#3344b8 70%,#1b2a9c 100%)}
.mission .heading{top:95px;width:100%;text-align:center;color:var(--white);font-size:40px}
.mission p{top:160px;left:150px;width:900px;text-align:center;color:var(--white);font-size:19px;line-height:34px}

/* about */
.about{top:1572px;height:584px}
.about .heading{left:616px;top:105px;font-size:40px;line-height:48px}
.about p{left:616px;top:215px;width:500px;font-size:13px;line-height:24px}
.btn-solid{background:var(--navy);color:var(--white);font-size:13px;font-weight:700;width:152px;height:50px;display:flex;align-items:center;justify-content:center;text-transform:uppercase}
.about .btn-solid{left:616px;top:383px}

/* pricing */
.pricing{top:2156px;height:497px;background:linear-gradient(180deg,#eeeeee,#fafafa)}
.pricing .heading{left:74px;top:125px;font-size:40px}
.pricing p{left:74px;top:197px;width:400px;font-size:13px;line-height:24px}
.pricing .btn-solid{left:74px;top:312px}
.price-table{left:616px;top:49px;width:511px}
.price-row{height:72px;display:flex;align-items:flex-start;font-size:14px;font-weight:600;font-style:italic;color:var(--navy);border-bottom:1px solid var(--line);padding-top:10px}
.price-row:last-child{border-bottom:none}
.price-row .t{width:230px;color:#222;font-style:normal}
.price-row .n{flex:1;text-transform:uppercase;font-weight:700}
.price-row .p{width:50px;text-align:right;font-weight:700}

/* testimonials */
.testimonials{top:2653px;height:549px}
.testi-media{position:absolute;inset:0;background:linear-gradient(180deg,#7d9fd4 0%,#a9bfdc 40%,#c6ced6 70%,#8f8f8f 100%)}
.testimonials .heading{left:74px;top:58px;font-size:42px;line-height:48px}
.testi-card{left:74px;top:179px;width:423px;height:301px;background:var(--white);padding:40px 26px}
.stars{display:flex;gap:6px}
.testi-card p{font-size:13px;line-height:24px;margin-top:10px}
.testi-card h4{font-style:italic;font-weight:800;font-size:14px;color:var(--navy);margin-top:12px}
.testi-arrow{left:456px;top:3095px}

/* before and after */
.before-after{top:3202px;height:581px}
.before-after .heading{top:55px;width:100%;text-align:center;font-size:40px}
.ba-tile{top:143px;height:365px}
.ba-tile span{position:absolute;left:12px;bottom:12px;color:var(--white);font-style:italic;font-weight:800;font-size:15px}
.ba-arrow{top:310px}

/* contact */
.contact{top:3783px;height:568px;background:linear-gradient(180deg,#1e33a8,#1629a0 60%,#13248f)}
.contact .heading{left:616px;top:100px;font-size:40px;color:var(--white)}
.field{background:var(--white);font-size:12px;color:#888;padding:14px 12px;position:absolute}
.contact .submit{left:616px;top:421px;width:152px;height:44px;background:#707070;color:var(--white);font-size:13px;font-weight:700;display:flex;align-items:center;justify-content:center}

/* footer */
.site-footer{top:4351px;height:370px}
.foot-brand{left:74px;top:92px;color:var(--navy);font-weight:700;font-size:22px;line-height:1.1}
.foot-brand small{display:block;font-size:12px;letter-spacing:2px}
.foot-copy{left:74px;top:166px;font-size:11px;line-height:24px;color:#222}
.socials{left:74px;top:244px;display:flex;gap:18px}
.socials span{width:16px;height:16px;border-radius:50%;background:var(--navy)}
.foot-col{top:60px}
.foot-col h5{font-style:italic;font-weight:800;font-size:17px;color:var(--navy);text-transform:uppercase;margin-bottom:8px}
.foot-col li{list-style:none;font-size:12px;line-height:28.5px;color:#222}
.contact-line{display:flex;align-items:center;gap:14px;font-size:12px;line-height:24px;color:#222;margin-bottom:16px}
.icon-ring{width:40px;height:40px;border-radius:50%;border:2px solid var(--navy);display:flex;align-items:center;justify-content:center;flex:none}
</style>
</head>
<body>

<header class="site-header">
  <div class="abs brand">Ridgecrest<small>RAPID WASH</small></div>
  <nav class="abs nav">
    <span class="active">Home</span><span>About Us</span><span>Why Ridgecrest</span><span>Services</span><span>Pricing</span><span>Videos</span><span>Fleets</span><span>Contact Us</span>
  </nav>
</header>

<section class="hero">
  <div class="hero-media" role="img" aria-label="Bus inside an automated wash bay lit in blue"></div>
  <h1 class="abs hero-title"><span class="l1">Ridgecrest</span><span class="l2">Rapid Wash</span></h1>
  <p class="abs hero-text">Temporibus autem quibusdam et aut officiis debitis aut rerum necessitatibus saepe eveniet ut et voluptates repudiandae sint.</p>
  <div class="abs hero-btns"><a class="btn-ghost">Book a Wash</a><a class="btn-ghost">Learn More</a><a class="btn-ghost">Contact Us</a></div>
  <div class="abs dots"><span class="on"></span><span></span><span></span><span></span></div>
</section>

<section class="services">
  <h2 class="abs heading">Our Services</h2>
  <div class="abs svc" style="left:58px">
    <div class="svc-ring"><div>
      <svg width="80" height="60" viewBox="0 0 80 60" fill="none" stroke="#fff" stroke-width="2.5"><rect x="10" y="22" width="30" height="22"/><rect x="40" y="28" width="20" height="16"/><circle cx="20" cy="48" r="5"/><circle cx="50" cy="48" r="5"/><path d="M44 28v8h16"/><path d="M14 8l2 4M22 4v5M30 8l-2 4"/></svg>
    </div></div>
    <h3>Automated Truck Wash</h3>
    <p>Excepteur sint occaecat cupidatat non proident, sunt in culpa qui officia deserunt mollit anim id est laborum.</p>
  </div>
  <div class="abs svc" style="left:419px">
    <div class="svc-ring"><div>
      <svg width="80" height="60" viewBox="0 0 80 60" fill="none" stroke="#fff" stroke-width="2.5"><path d="M30 46V14h24l10 14v18z"/><path d="M54 14v14h10"/><circle cx="38" cy="48" r="5"/><circle cx="58" cy="48" r="5"/><circle cx="22" cy="36" r="10"/><path d="M14 10l2 3M22 6v4"/></svg>
    </div></div>
    <h3>Additional Services</h3>
    <p>Excepteur sint occaecat cupidatat non proident, sunt in culpa qui officia deserunt mollit anim id est laborum.</p>
  </div>
  <div class="abs svc" style="left:780px">
    <div class="svc-ring"><div>
      <svg width="80" height="60" viewBox="0 0 80 60" fill="none" stroke="#fff" stroke-width="2.5"><path d="M16 36l6-14h36l6 14v10H16z"/><circle cx="26" cy="40" r="3"/><circle cx="54" cy="40" r="3"/><path d="M18 46v6M62 46v6"/><circle cx="40" cy="12" r="6"/></svg>
    </div></div>
    <h3>Fleet Services</h3>
    <p>Excepteur sint occaecat cupidatat non proident, sunt in culpa qui officia deserunt mollit anim id est laborum.</p>
  </div>
</section>

<section class="mission">
  <div class="mission-media" role="img" aria-label="Bus passing through rotating wash brushes, tinted blue"></div>
  <h2 class="abs heading">Our Mission</h2>
  <p class="abs">Sed ut perspiciatis unde omnis iste natus error sit voluptatem accusantium doloremque laudantium, totam rem aperiam, eaque ipsa quae ab illo inventore veritatis et quasi architecto beatae vitae dicta sunt explicabo. Nemo enim ipsam voluptatem quia voluptas sit aspernatur aut odit aut fugit, sed quia consequuntur magni dolores eos qui ratione voluptatem.</p>
</section>

<section class="about">
  <svg class="abs" style="left:74px;top:53px" width="512" height="445" viewBox="0 0 512 445">
    <polygon points="16,0 512,40 512,445 60,445" fill="#0a1478"/>
    <polygon points="0,40 512,15 512,408 0,390" fill="#fff"/>
  </svg>
  <div class="abs" role="img" aria-label="Blue semi truck parked in a wash bay" style="left:74px;top:68px;width:512px;height:392px;background:linear-gradient(135deg,#3c8a86,#3b69b8 40%,#1f4a9a 65%,#5a6470);clip-path:polygon(0 7%,100% 0,100% 100%,0 95%)"></div>
  <h2 class="abs heading">About Ridgecrest<br>Rapid Wash</h2>
  <p class="abs">Sed ut perspiciatis unde omnis iste natus error sit voluptatem accusantium doloremque laudantium, totam rem aperiam, eaque ipsa quae ab illo inventore veritatis et quasi architecto beatae vitae dicta sunt explicabo. Nemo enim ipsam voluptatem quia voluptas sit aspernatur aut odit aut fugit, sed quia consequuntur magni dolores eos qui ratione voluptatem.</p>
  <a class="abs btn-solid">Read More</a>
</section>

<section class="pricing">
  <h2 class="abs heading">Pricing Packages</h2>
  <p class="abs">Sed ut perspiciatis unde omnis istatus error sit v oluptatem ccusantium doloremque laudantiumtam rem aperiam, eaque ipsa quae ab illo inventoreritatis et quasi architecto beatae</p>
  <a class="abs btn-solid">View Pricing</a>
  <div class="abs price-table">
    <div class="price-row"><span class="t">12:00- 9:30PM</span><span class="n">Basic Wash</span><span class="p">$45</span></div>
    <div class="price-row"><span class="t">12:00- 9:30PM</span><span class="n">Standard</span><span class="p">$45</span></div>
    <div class="price-row"><span class="t">12:00- 9:30PM</span><span class="n">Standard Plus</span><span class="p">$45</span></div>
    <div class="price-row"><span class="t">12:00- 9:30PM</span><span class="n">Premium</span><span class="p">$45</span></div>
    <div class="price-row"><span class="t">12:00- 9:30PM</span><span class="n">Polymer Pro</span><span class="p">$90</span></div>
    <div class="price-row"><span class="t">12:00- 9:30PM</span><span class="n">Wash &amp; Wax</span><span class="p">$461</span></div>
  </div>
</section>

<section class="testimonials">
  <div class="testi-media" role="img" aria-label="White semi truck with trailer on a highway below mountains"></div>
  <h2 class="abs heading">Customer<br>Testimonials</h2>
  <div class="abs testi-card">
    <div class="stars">
      <svg width="90" height="14" viewBox="0 0 90 14" fill="#f07a1a"><g id="s"><polygon points="7,0 9,5 14,5 10,8 11.5,13 7,10 2.5,13 4,8 0,5 5,5"/></g><use href="#s" x="19"/><use href="#s" x="38"/><use href="#s" x="57"/><use href="#s" x="76"/></svg>
    </div>
    <p>Sed ut perspiciatis unde omnis iste natus error sit voluptatem accusantium doloremque laudantium, totam rem aperiam, eaque ipsa quae ab illo inventore veritatis et quasi architecto beatae vitae dicta sunt explicabo. Nemo enim ipsam voluptatem quia voluptas sit aspernatur aut odit aut fugit, sed quia consequuntur magni dolores eos qui.”</p>
    <h4>NAME HEADING</h4>
  </div>
  <svg class="abs" style="left:456px;top:442px" width="56" height="56" viewBox="0 0 56 56"><circle cx="28" cy="28" r="27" fill="#0a1478" stroke="#fff" stroke-width="2"/><path d="M24 20l-8 8 8 8M32 20l8 8-8 8" fill="none" stroke="#fff" stroke-width="2.5"/></svg>
</section>

<section class="before-after">
  <h2 class="abs heading">Before &amp; After</h2>
  <div class="abs ba-tile" role="img" aria-label="Clean red semi truck in a wash bay" style="left:0;width:267px;background:linear-gradient(135deg,#c9cfd6,#8a2a30 55%,#5a5f66)"><span>AFTER</span></div>
  <div class="abs ba-tile" role="img" aria-label="Dirty bus front before washing" style="left:317px;width:282px;background:linear-gradient(180deg,#6a7a8a,#b5b29a 55%,#8d8c80)"><span>BEFORE</span></div>
  <div class="abs ba-tile" role="img" aria-label="Clean bus front after washing" style="left:601px;width:282px;background:linear-gradient(180deg,#5d6a7a,#c9cdd2 55%,#9aa0a6)"><span>AFTER</span></div>
  <div class="abs ba-tile" role="img" aria-label="Muddy truck wheels before washing" style="left:932px;width:268px;background:linear-gradient(135deg,#8a3a2a,#5a4a40 50%,#a08070)"><span>BEFORE</span></div>
  <svg class="abs" style="left:589px;top:3548px;top:346px" width="22" height="1" ></svg>
  <svg class="abs ba-arrow" style="left:578px" width="42" height="42" viewBox="0 0 42 42"><circle cx="21" cy="21" r="20" fill="#fff"/><path d="M17 14l-6 7 6 7M25 14l6 7-6 7" fill="none" stroke="#555" stroke-width="2"/><path d="M21 10v22" stroke="#555" stroke-width="1.5"/></svg>
  <svg class="abs ba-arrow" style="left:275px" width="28" height="42" viewBox="0 0 28 42"><path d="M20 4L6 21l14 17" fill="none" stroke="#111" stroke-width="3"/></svg>
  <svg class="abs ba-arrow" style="left:895px" width="28" height="42" viewBox="0 0 28 42"><path d="M8 4l14 17L8 38" fill="none" stroke="#111" stroke-width="3"/></svg>
</section>

<section class="contact">
  <svg class="abs" style="left:74px;top:62px" width="490" height="445" viewBox="0 0 490 445"><polygon points="60,0 490,20 490,445 0,420 20,80" fill="#8c8c8c"/></svg>
  <div class="abs" role="img" aria-label="Truck entering a wash bay between red and black rotating brushes" style="left:74px;top:84px;width:490px;height:400px;background:linear-gradient(90deg,#b8bcc4,#8a1d2a 20%,#d9dde2 50%,#8a1d2a 80%,#b8bcc4);clip-path:polygon(0 5%,100% 0,100% 100%,0 92%)"></div>
  <h2 class="abs heading">Contact Us</h2>
  <div class="field" style="left:616px;top:176px;width:247px;height:46px">First Name</div>
  <div class="field" style="left:894px;top:176px;width:233px;height:46px">Last Name</div>
  <div class="field" style="left:616px;top:236px;width:247px;height:46px">Email Address</div>
  <div class="field" style="left:894px;top:236px;width:233px;height:46px">Phone No</div>
  <div class="field" style="left:616px;top:295px;width:511px;height:108px">Message</div>
  <a class="abs submit">SUBMIT</a>
</section>

<footer class="site-footer">
  <div class="abs foot-brand">Ridgecrest<small>RAPID WASH</small></div>
  <div class="abs foot-copy">© 2024 Company Name<br>All Rights Reserved. Privacy policy</div>
  <div class="abs socials" aria-label="Social media links"><span></span><span></span><span></span><span></span><span></span></div>
  <div class="abs foot-col" style="left:412px">
    <h5>Quick Links</h5>
    <ul><li>Home</li><li>About us</li><li>Why Ridgecrest</li><li>Services</li><li>Pricing</li><li>Videos of Wash System</li><li>Fleets</li><li>Contact us</li></ul>
  </div>
  <div class="abs foot-col" style="left:665px">
    <h5>Services</h5>
    <ul><li>Automated Truck Wash</li><li>Additional Services</li><li>Fleet Services</li></ul>
  </div>
  <div class="abs foot-col" style="left:885px">
    <h5>Contact Info</h5>
    <div class="contact-line"><span class="icon-ring"><svg width="16" height="16" viewBox="0 0 16 16"><path d="M8 1a5 5 0 0 0-5 5c0 4 5 9 5 9s5-5 5-9a5 5 0 0 0-5-5z" fill="#0a1478"/><circle cx="8" cy="6" r="2" fill="#fff"/></svg></span><span>48 Harbor Lane Suite 12,<br>Dayton 45402, United States</span></div>
    <div class="contact-line"><span class="icon-ring"><svg width="16" height="16" viewBox="0 0 16 16"><path d="M4 1l3 3-2 2c1 2 3 4 5 5l2-2 3 3-2 3C7 15 1 9 1 3z" fill="#0a1478"/></svg></span><span>+1-555-014-2290</span></div>
    <div class="contact-line"><span class="icon-ring"><svg width="16" height="16" viewBox="0 0 16 16"><rect x="1" y="3" width="14" height="10" fill="#0a1478"/><path d="M1 3l7 6 7-6" fill="none" stroke="#fff" stroke-width="1.3"/></svg></span><span>info@ridgecrestwash.com</span></div>
  </div>
</footer>

</body>
</html>
```